business card design for a small scale specialty cut flower farm

We need a business card design for Hollowmere Blossom Farm based in Langley, BC, Canada. We produce specialty, high-end cut flowers and sell locally to florists, local shops and markets and the end user through bouquet subscriptions. The final business card design should be memorable and have a timeless or vintage feel. We would prefer a square shape.

Target Market(s)

florists, shops and seasonal markets, local flower lovers

Industry/Entity Type

Floral

Contact Information for Business Card

Maren Tilde Hofstad, Grower
Langley, BC, Canada
website: hollowmereblossomfarm.com
instagram: @hollowmereblossomfarm
Tel: 604.913.2748
facebook: www.facebook.com/hollowmereblooms/

Font styles to use
Serif
Decorative
Script

Requirements
Must have
• soft black background colour on front side, the included logo and catch phrase: Fresh Local Seasonal
Nice to have
• phone number and website address on front of card, included photo 6539 incorporated onto the back, possibly photo 6609 as well.

```html
<!DOCTYPE html>
<html lang="en">
<head>
<meta charset="utf-8">
<title>Hollowmere Blossom Farm – Business Card</title>
<link rel="stylesheet" href="https://fonts.googleapis.com/css2?family=Allura&family=Montserrat:wght@300;400&display=swap">
<style>
  :root {
    --stage: #e4e2df;
    --soft-black: #2a2a2a;
    --ink-light: #ffffff;
    --ink-muted: #c9c6c2;
    --accent-pink: #e7a1c4;
    --edge-green: #6f8f4a;
    --photo-rose: #c94a6a;
    --photo-wine: #5a1f33;
    --photo-coral: #e8767a;
    --photo-violet: #7a5a9a;
    --photo-leaf: #6e8a4e;
  }
  * { margin: 0; padding: 0; box-sizing: border-box; }
  html, body { width: 1200px; height: 801px; overflow: hidden; }
  body {
    background: var(--stage);
    font-family: "Montserrat", sans-serif;
    position: relative;
  }
  .card {
    position: absolute;
    width: 540px;
    height: 309px;
    border-bottom: 2px solid var(--edge-green);
    box-shadow: 0 6px 18px rgba(0,0,0,0.18);
    overflow: hidden;
  }
  .card--front { left: 40px; top: 246px; background: var(--soft-black); }
  .card--back { left: 620px; top: 246px; }

  /* shared wordmark */
  .brand {
    display: flex; flex-direction: column; align-items: center;
    color: var(--ink-light); text-align: center;
  }
  .brand-name {
    font-weight: 300; letter-spacing: 0.24em; text-transform: uppercase;
    font-size: 20px; line-height: 1.35;
  }
  .brand-tagline {
    font-family: "Allura", cursive;
    font-size: 21px; line-height: 1; margin-top: 4px;
    color: var(--ink-muted);
  }
  .brand-est {
    font-weight: 300; font-size: 8px; letter-spacing: 0.45em;
    color: var(--ink-muted); margin-top: 6px;
  }

  /* front */
  .card--front .brand { position: absolute; left: 0; right: 0; top: 58px; }
  .contact-list {
    position: absolute; left: 30px; right: 30px; bottom: 28px;
    display: grid; grid-template-columns: auto auto; gap: 9px 22px;
    justify-content: center;
    list-style: none; color: var(--ink-light);
    font-size: 12.5px; font-weight: 300;
  }
  .contact-list li { display: flex; align-items: center; gap: 6px; }
  .contact-icon { width: 11px; height: 11px; flex: none; }

  /* back */
  .flower-photo {
    position: absolute; inset: 0;
    background:
      radial-gradient(circle at 78% 30%, var(--photo-coral) 0 12%, transparent 30%),
      radial-gradient(circle at 88% 70%, var(--photo-wine) 0 15%, transparent 35%),
      radial-gradient(circle at 12% 75%, #e35b94 0 14%, transparent 30%),
      radial-gradient(circle at 45% 85%, #ee9a9a 0 12%, transparent 28%),
      radial-gradient(circle at 55% 15%, var(--photo-violet) 0 10%, transparent 28%),
      radial-gradient(circle at 30% 20%, var(--photo-leaf) 0 10%, transparent 28%),
      linear-gradient(135deg, #8a5a78, var(--photo-rose) 50%, var(--photo-wine));
  }
  .card--back .brand {
    position: absolute; left: 80px; top: 92px;
    text-shadow: 0 1px 4px rgba(0,0,0,0.35);
  }
  .card--back .brand-name { font-size: 24px; }
  .card--back .brand-tagline { color: var(--ink-light); font-size: 24px; }
  .catchphrase {
    position: absolute; left: 0; right: 0; bottom: 40px; text-align: center;
    color: var(--ink-light); font-weight: 400; font-size: 17px; letter-spacing: 0.12em;
    text-shadow: 0 1px 4px rgba(0,0,0,0.4);
  }
</style>
</head>
<body>
  <section class="card card--front" aria-label="Card front">
    <div class="brand">
      <p class="brand-name">Hollowmere<br>Blossom Farm</p>
      <p class="brand-tagline">Specialty Cut Flowers</p>
      <p class="brand-est">EST. 2019</p>
    </div>
    <ul class="contact-list">
      <li>
        <svg class="contact-icon" viewBox="0 0 12 12"><path d="M3 1 L5 3.5 L4 5 Q5 7 7 8 L8.5 7 L11 9 L10 11 Q4 11 1 3 Z" fill="var(--accent-pink)"/></svg>
        604.913.2748
      </li>
      <li>
        <svg class="contact-icon" viewBox="0 0 12 12"><circle cx="6" cy="6" r="5" fill="var(--accent-pink)"/></svg>
        hollowmereblossomfarm.com
      </li>
      <li>
        <svg class="contact-icon" viewBox="0 0 12 12"><circle cx="6" cy="6" r="5" fill="var(--accent-pink)"/></svg>
        @hollowmereblossomfarm
      </li>
      <li>
        <svg class="contact-icon" viewBox="0 0 12 12"><rect x="1" y="1" width="10" height="10" fill="var(--accent-pink)"/></svg>
        /hollowmereblooms
      </li>
    </ul>
  </section>

  <section class="card card--back" aria-label="Card back">
    <div class="flower-photo" role="img" aria-label="Photo of dahlias, hydrangeas and mixed cut flowers in buckets"></div>
    <div class="brand">
      <p class="brand-name">Hollowmere<br>Blossom Farm</p>
      <p class="brand-tagline">Specialty Cut Flowers</p>
    </div>
    <p class="catchphrase">Fresh | Local | Seasonal</p>
  </section>
</body>
</html>
```